Training Consultant for Oil and Gas Drillers needs logo for business cards

I teach oil and gas professionals the skills required to keep rigs from blowing up. The company name is "Night Shift Bore Safety", which is pronounced Nite Shiffed. Tour refers to the time on an oil rig when a worker is off for sleep and rest. I teach something called Well Control, which is how to maintain a pressure balance in the well so the hydro carbons don't come to surface unexpectedly( like the Grey Tide Platform).

Target Market(s)

Rig hands and oil companies

Contact Information for Business Card

Night Shift BS ( company name) with a new logo
My name (Derek Holloway )and Title (Well Control Consultant)
Phone number and address

Font styles to use
Serif
Sans Serif

Colors

Designer to choose colors to be used in the design.

Requirements
Must have
• I need a logo for the company. I do not have anything yet

```html
<!DOCTYPE html>
<html lang="en">
<head>
<meta charset="UTF-8">
<title>Night Shift BS – Business Card</title>
<link rel="stylesheet" href="https://fonts.googleapis.com/css2?family=Montserrat:wght@700&family=Work+Sans:wght@400;500&display=swap">
<style>
  :root {
    --backdrop: #1c1c1e;
    --card: #232325;
    --card-edge: #2c2c2f;
    --white: #f4f4f4;
    --silver: #a9a9ad;
    --blue: #2199d8;
  }
  * { margin: 0; padding: 0; box-sizing: border-box; }
  html, body {
    width: 1200px; height: 900px; overflow: hidden;
    background: var(--backdrop);
  }
  .stage {
    position: relative; width: 1200px; height: 900px;
    display: flex; flex-direction: column; align-items: center; justify-content: center; gap: 36px;
  }
  .card {
    position: relative; width: 620px; height: 354px;
    background: linear-gradient(135deg, var(--card) 0%, var(--card-edge) 100%);
    box-shadow: 0 14px 30px rgba(0,0,0,.55);
  }
  /* front */
  .card--front {
    display: flex; flex-direction: column; align-items: center; justify-content: center; gap: 18px;
  }
  .brand-dot {
    width: 96px; height: 96px; border-radius: 50%;
    background: linear-gradient(135deg, #6e6e72, #2e2e31);
  }
  .brand-name {
    font-family: "Montserrat", sans-serif; font-weight: 700;
    font-size: 42px; letter-spacing: 1px; white-space: nowrap;
  }
  .card--front .brand-name { color: var(--silver); }
  /* back */
  .card--back { display: flex; align-items: center; }
  .brand-block {
    width: 300px; display: flex; flex-direction: column; align-items: center; gap: 16px;
  }
  .card--back .brand-dot {
    width: 92px; height: 92px; background: var(--blue);
  }
  .card--back .brand-name { color: var(--white); font-size: 36px; }
  .divider {
    width: 2px; height: 176px; background: var(--white); margin: 0 30px 0 6px;
  }
  .contact {
    font-family: "Work Sans", sans-serif; color: var(--white);
    font-size: 16px; letter-spacing: 1px; line-height: 1.35;
  }
  .contact__name {
    color: var(--blue); font-size: 22px; font-weight: 500; letter-spacing: 1.5px;
    text-transform: uppercase;
  }
  .contact__title { margin-bottom: 12px; }
  .contact__address { margin-bottom: 12px; }
  .contact__line { display: flex; align-items: center; gap: 10px; }
  .contact__line svg { width: 13px; height: 13px; flex: none; }
  .accent { color: var(--blue); }
</style>
</head>
<body>
<main class="stage">
  <section class="card card--front">
    <div class="brand-dot"></div>
    <div class="brand-name">Night Shift BS</div>
  </section>

  <section class="card card--back">
    <div class="brand-block">
      <div class="brand-dot"></div>
      <div class="brand-name">Night Shift BS</div>
    </div>
    <div class="divider"></div>
    <div class="contact">
      <div class="contact__name">Derek Holloway</div>
      <div class="contact__title">Well Control Consultant</div>
      <div class="contact__address">1180 Ridgeline Ct.<br>Midvale, TX 75390</div>
      <div class="contact__line">
        <svg viewBox="0 0 16 16" aria-hidden="true"><path d="M3 1h3l1.5 4-2 1.2a9 9 0 0 0 4.3 4.3L11 8.5l4 1.5v3a2 2 0 0 1-2 2A13 13 0 0 1 1 3a2 2 0 0 1 2-2z" fill="var(--blue)"/></svg>
        <span>1300 642 917</span>
      </div>
      <div class="contact__line">
        <svg viewBox="0 0 16 16" aria-hidden="true"><rect x="1.5" y="3.5" width="13" height="9" fill="none" stroke="var(--blue)" stroke-width="1.5"/><path d="M1.5 3.5 8 9l6.5-5.5" fill="none" stroke="var(--blue)" stroke-width="1.5"/></svg>
        <span>info@nightshiftbs.com</span>
      </div>
      <div class="contact__line">
        <svg viewBox="0 0 16 16" aria-hidden="true"><circle cx="8" cy="8" r="6.5" fill="none" stroke="var(--blue)" stroke-width="1.4"/><path d="M1.5 8h13M8 1.5c-3 3.5-3 9.5 0 13M8 1.5c3 3.5 3 9.5 0 13" fill="none" stroke="var(--blue)" stroke-width="1.2"/></svg>
        <span>www.<span class="accent">nightshiftbs</span>.com</span>
      </div>
    </div>
  </section>
</main>
</body>
</html>
```